Business card needed for home based pen making business.

I'm after a business card that's a bit more than an off the shelf card. I do like the idea of a card split horizontal with different colours used. A third colour is to be used for the business name and if need a forth for the other details.

I don't have a logo and will pay extra for one ($150 extra). I mainly make pens and seam rippers (stitch unpicks). The logo may be used for a website in future, as will the colours so please provide the colour codes and font type.

I'd like the business name in an easy to read script font at the top (with logo if you have one) and the other details to the bottom left hand side. I'll leave it up to you to match the script to the font used for the other details.

I'd like to keep a triangular balance to the card so something like a siloet of pot containing pens on the bottom right could be used to balance it out. There my ideas I want to see your.

Business name: Quill & Co
Email address: quillandco@mailbox-example.net
Contact: Trevor
Phone: 0412 555 874
No address is to be used on card.

Target Market(s)

Wide variety of people visiting craft markets. Age range 30+.

Industry/Entity Type

Business

Contact Information for Business Card

Quill & Co

Font styles to use
Script

Colors
f0ecf4
3277b5
3176b5

Requirements
Must have
• Contact: Trevor
• Phone: 0412 555 874
• Email address: quillandco@mailbox-example.net
Nice to have
• An icon and/or graphics depicting pens and seam rippers..
Should not have
• I don't want icon/ graphic to be a crossed pen and seam ripper.

```html
<!DOCTYPE html>
<html lang="en">
<head>
<meta charset="utf-8">
<title>Quill &amp; Co — Business Card</title>
<link rel="stylesheet" href="https://fonts.googleapis.com/css2?family=Arimo:wght@400&family=Kaushan+Script&display=swap">
<style>
  :root {
    --page-bg: #e9e6ec;
    --card-bg: #f0ecf4;
    --band-blue: #3b84c4;
    --brand-blue: #3277b5;
    --name-blue: #3176b5;
    --tint-band: #d3ebf2;
    --icon-dark: #2e48a4;
    --icon-mid: #3553b0;
    --icon-light: #5a7cc8;
    --detail-text: #3a5fae;
    --icon-stroke: #ffffff;
  }
  * { margin: 0; padding: 0; box-sizing: border-box; }
  html, body {
    width: 1200px;
    height: 720px;
    overflow: hidden;
    background: var(--page-bg);
    font-family: "Arimo", Arial, sans-serif;
  }
  .canvas {
    width: 1200px;
    height: 720px;
    display: flex;
    align-items: center;
    justify-content: center;
  }
  .business-card {
    position: relative;
    width: 380px;
    height: 620px;
    background: var(--card-bg);
    box-shadow: 0 2px 10px rgba(0,0,0,0.12);
    overflow: hidden;
  }
  .side-band {
    position: absolute;
    left: 0; top: 0;
    width: 84px;
    height: 410px;
    background: var(--band-blue);
  }
  .icon-column {
    position: absolute;
    left: 0; top: 410px;
    width: 84px;
  }
  .icon-tile {
    width: 84px;
    height: 62px;
    display: flex;
    align-items: center;
    justify-content: center;
  }
  .icon-tile--person { background: var(--icon-dark); }
  .icon-tile--phone { background: var(--icon-mid); }
  .icon-tile--link { background: var(--icon-light); }
  .icon-tile svg { width: 38px; height: 38px; }
  .brand {
    position: absolute;
    left: 84px; right: 0;
    top: 80px;
    display: flex;
    flex-direction: column;
    align-items: center;
    gap: 36px;
  }
  .brand-dot {
    width: 110px;
    height: 110px;
    border-radius: 50%;
    background: var(--brand-blue);
  }
  .brand-name {
    font-family: "Kaushan Script", cursive;
    font-size: 40px;
    font-weight: 400;
    line-height: 1.1;
    color: var(--brand-blue);
    white-space: nowrap;
  }
  .name-band {
    position: absolute;
    left: 84px; right: 0;
    top: 330px;
    height: 80px;
    background: var(--tint-band);
  }
  .contact-name {
    position: absolute;
    left: 108px;
    top: 370px;
    font-size: 24px;
    line-height: 1;
    color: var(--name-blue);
  }
  .contact-detail {
    position: absolute;
    left: 108px;
    font-size: 15px;
    line-height: 1;
    color: var(--detail-text);
    letter-spacing: 0.3px;
  }
  .contact-detail--phone { top: 458px; }
  .contact-detail--email { top: 508px; font-size: 14px; }
</style>
</head>
<body>
<main class="canvas">
  <article class="business-card">
    <div class="side-band"></div>

    <div class="brand">
      <div class="brand-dot"></div>
      <div class="brand-name">Quill &amp; Co</div>
    </div>

    <div class="name-band"></div>
    <p class="contact-name">Trevor</p>
    <p class="contact-detail contact-detail--phone">0412 555 874</p>
    <p class="contact-detail contact-detail--email">quillandco@mailbox-example.net</p>

    <div class="icon-column">
      <div class="icon-tile icon-tile--person">
        <svg viewBox="0 0 40 40" fill="none" stroke="var(--icon-stroke)" stroke-width="2">
          <circle cx="20" cy="20" r="17"/>
          <circle cx="20" cy="16" r="6"/>
          <path d="M9 31c2-6 7-8 11-8s9 2 11 8"/>
        </svg>
      </div>
      <div class="icon-tile icon-tile--phone">
        <svg viewBox="0 0 40 40" fill="none" stroke="var(--icon-stroke)" stroke-width="2">
          <path d="M5 14c0-5 7-7 15-7s15 2 15 7l-5 2-2-4c-5-1-11-1-16 0l-2 4z"/>
          <path d="M10 20h20l3 12H7z"/>
          <circle cx="15" cy="24" r="1.6"/><circle cx="20" cy="24" r="1.6"/><circle cx="25" cy="24" r="1.6"/>
          <circle cx="15" cy="29" r="1.6"/><circle cx="20" cy="29" r="1.6"/><circle cx="25" cy="29" r="1.6"/>
        </svg>
      </div>
      <div class="icon-tile icon-tile--link">
        <svg viewBox="0 0 40 40" fill="none" stroke="var(--icon-stroke)" stroke-width="2.2">
          <rect x="6" y="15" width="16" height="10" rx="5" transform="rotate(-45 14 20)"/>
          <rect x="18" y="15" width="16" height="10" rx="5" transform="rotate(-45 26 20)"/>
        </svg>
      </div>
    </div>
  </article>
</main>
</body>
</html>
```